Pro-life non-profit needs a dynamic poster design for their Christmas Gala.

We need a poster design which plays off the name of the event, The Winter Lantern. The Winter Lantern, of course is the Baby Jesus. Our cause supports unborn children in Iowa. The gala will include a concert of popular Christmas music sung by top soloists backed by an orchestra. An original commissioned song, The Winter Lantern, will be premiered. Purple and gold colors immediately come to mind, but a designer should not feel constrained on colors. We need an editable design w/fonts. Photoshop w/layers or Illustrator files are good.

```html
<!DOCTYPE html>
<html lang="en">
<head>
<meta charset="utf-8">
<title>The Winter Lantern – A Pro-Life Christmas Gala</title>
<link rel="stylesheet" href="https://fonts.googleapis.com/css2?family=Open+Sans:ital,wght@1,300;1,400&family=Great+Vibes&family=Josefin+Sans:wght@400;600&family=Cabin:wght@400;500&family=Cinzel:wght@400&display=swap">
<style>
  :root {
    --night-deep: #3a0758;
    --night-mid: #5a1280;
    --night-glow: #e6b8fa;
    --dune-dark: #3f0a5c;
    --dune-mid: #5c1a82;
    --dune-light: #a25fc7;
    --dune-pale: #c27fe0;
    --silhouette: #230530;
    --lime-gold: #c3d92b;
    --cream: #f4ecd6;
    --ink-plum: #2a0838;
    --frame-gold: #a9ae2a;
  }
  * { margin: 0; padding: 0; box-sizing: border-box; }
  html, body { width: 849px; height: 1200px; overflow: hidden; }
  body { background: var(--night-deep); }

  .poster {
    position: relative;
    width: 849px;
    height: 1200px;
    overflow: hidden;
    color: var(--cream);
  }

  .sky {
    position: absolute;
    inset: 0;
    background:
      radial-gradient(ellipse 300px 260px at 60px 540px, rgba(245,215,255,0.95), rgba(210,150,240,0.55) 45%, transparent 80%),
      linear-gradient(180deg, #5a147f 0%, #520e78 40%, #4a0c6e 100%);
  }
  .dunes { position: absolute; inset: 0; }

  .nativity-art, .traveller-art {
    position: absolute;
  }
  .nativity-art {
    left: 40px; top: 330px; width: 290px; height: 360px;
    background: radial-gradient(ellipse 50% 55% at 50% 55%, rgba(35,5,48,0.9), rgba(35,5,48,0.55) 60%, transparent 100%);
  }
  .traveller-art {
    left: 410px; top: 430px; width: 439px; height: 520px;
    background: radial-gradient(ellipse 42% 50% at 68% 48%, rgba(35,5,48,0.88), rgba(35,5,48,0.5) 60%, transparent 100%);
  }

  .block { position: absolute; left: 0; width: 100%; text-align: center; }

  .presenter {
    font-family: "Open Sans", sans-serif;
    font-style: italic;
    font-weight: 300;
    font-size: 22px;
    letter-spacing: 3px;
    line-height: 33px;
    top: 48px;
  }

  .title-the {
    top: 160px; left: 262px; width: 430px;
    font-family: "Josefin Sans", sans-serif;
    font-size: 44px; letter-spacing: 3px;
    color: var(--lime-gold);
  }
  .title-script {
    left: 262px; width: 430px;
    font-family: "Great Vibes", cursive;
    color: var(--lime-gold);
    text-shadow: -5px 4px 0 rgba(20, 4, 30, 0.55);
    line-height: 1;
  }
  .title-winter { top: 190px; font-size: 142px; }
  .title-lantern { top: 318px; font-size: 130px; }

  .subtitle {
    left: 262px; width: 430px;
    font-family: "Josefin Sans", sans-serif;
    font-size: 29px; letter-spacing: 4px; line-height: 38px;
    color: var(--lime-gold);
    top: 448px;
    text-shadow: -2px 2px 0 rgba(20, 4, 30, 0.5);
  }

  .details-frame { position: absolute; left: 173px; top: 730px; width: 490px; height: 256px; }
  .details {
    font-family: "Cabin", sans-serif;
    font-size: 22px; line-height: 30px;
    color: var(--cream);
    text-shadow: 1px 1px 2px rgba(20, 4, 30, 0.8);
    top: 750px; left: 173px; width: 490px;
  }
  .details p + p { margin-top: 29px; }

  .speaker-label {
    top: 1010px;
    font-family: "Cabin", sans-serif; font-weight: 500;
    font-size: 24px; letter-spacing: 8px;
    color: var(--cream);
    text-shadow: 0 0 3px var(--ink-plum), 1px 1px 2px var(--ink-plum);
  }
  .speaker-name {
    top: 1042px;
    font-family: "Josefin Sans", sans-serif; font-weight: 600;
    font-size: 31px; letter-spacing: 4px;
    color: var(--lime-gold);
    text-shadow: -2px 2px 0 var(--ink-plum);
  }
  .seating {
    top: 1097px;
    font-family: "Cinzel", serif;
    font-size: 19px; letter-spacing: 4px;
    color: var(--ink-plum);
  }
  .contact {
    top: 1134px;
    font-family: "Cabin", sans-serif;
    font-size: 21px; line-height: 29px; letter-spacing: 0.5px;
    color: var(--ink-plum);
  }
</style>
</head>
<body>
<main class="poster">
  <div class="sky"></div>
  <svg class="dunes" width="849" height="1200" viewBox="0 0 849 1200" aria-hidden="true">
    <path d="M0 615 C160 640 330 660 460 650 C600 640 740 690 849 720 V1200 H0 Z" fill="var(--dune-mid)"/>
    <path d="M0 700 C200 690 420 730 600 790 C700 820 790 860 849 880 V1200 H0 Z" fill="var(--dune-dark)"/>
    <path d="M0 870 C120 875 200 960 330 1010 C470 1060 640 1010 849 1000 V1200 H0 Z" fill="var(--dune-light)"/>
    <path d="M640 900 C700 890 740 930 700 1020 L849 1010 V930 C780 900 700 880 640 900 Z" fill="var(--dune-pale)"/>
    <path d="M0 1060 C250 1090 560 1070 849 1040 V1200 H0 Z" fill="#9a52c0"/>
  </svg>

  <div class="nativity-art" role="img" aria-label="Silhouette of a lit stable with the Holy Family and the newborn child in the manger"></div>
  <div class="traveller-art" role="img" aria-label="Silhouette of a traveller leading a camel with a rider across the dunes"></div>

  <p class="block presenter">Heartland for LIFE<br>presents the Tenth Annual Fundraising Banquet</p>

  <p class="block title-the">THE</p>
  <h1>
    <span class="block title-script title-winter">Winter</span>
    <span class="block title-script title-lantern">Lantern</span>
  </h1>
  <p class="block subtitle">A PRO-LIFE<br>CHRISTMAS GALA</p>

  <svg class="details-frame" width="490" height="256" viewBox="0 0 490 256" aria-hidden="true">
    <path d="M227 1.5 H1.5 V254.5 H488.5 V1.5 H279" fill="none" stroke="var(--frame-gold)" stroke-width="3"/>
  </svg>
  <div class="block details">
    <p>Saturday, November 21st, 2020<br>Doors open at 5:30 PM<br>Harmon Hall Center, Maple Grove, IA</p>
    <p>$60 person &#9679; $500 table of ten</p>
    <p>Cocktails &#9679; Dinner &#9679; Christmas Concert</p>
  </div>

  <p class="block speaker-label">SPECIAL GUEST SPEAKER:</p>
  <p class="block speaker-name">BISHOP THOMAS ALDRIDGE</p>

  <p class="block seating">SEATING LIMITED &#8226; RESERVATIONS NEEDED</p>
  <p class="block contact">Order tickets online: www.HeartlandForLife.org<br>515-555-0142 &#8226; mlarsen@heartlandforlife.org</p>
</main>
</body>
</html>
```